Domestic Services and Home Organisation Business Flyer

Font styles to use
Serif
Decorative
Script

Colors
b666a9
86cfc6
eaf2ce
b7a5cd
f3f1f8
e4daeb
d3a5cc
cee9f5

```html
<!DOCTYPE html>
<html lang="en">
<head>
<meta charset="utf-8">
<title>Tidy Nest Haven – Domestic Cleaning Flyer</title>
<link href="https://fonts.googleapis.com/css2?family=Courgette&family=Questrial&display=swap" rel="stylesheet">
<style>
  :root {
    --teal: #86cfc6;
    --teal-deep: #5dbcae;
    --lime: #eaf2ce;
    --leaf: #6bb04a;
    --paper: #f7f7f5;
    --stage: #e6e3de;
    --ink: #555a5c;
    --ink-soft: #8a8f91;
    --white: #ffffff;
  }
  html, body {
    margin: 0;
    padding: 0;
    width: 921px;
    height: 1200px;
    overflow: hidden;
    background: var(--stage);
  }
  .flyer {
    position: absolute;
    left: 35px;
    top: 0;
    width: 850px;
    height: 1200px;
    background: var(--paper);
    overflow: hidden;
    font-family: "Questrial", sans-serif;
  }
  .brand-mark {
    position: absolute;
    left: 62px;
    top: 36px;
    width: 60px;
    height: 60px;
    border-radius: 50%;
    background: var(--leaf);
  }
  .brand-name {
    position: absolute;
    left: 130px;
    top: 22px;
    width: 540px;
    margin: 0;
    text-align: center;
    font-family: "Courgette", cursive;
    font-weight: 400;
    font-size: 60px;
    line-height: 1.1;
    color: var(--teal-deep);
  }
  .brand-claim {
    position: absolute;
    left: 150px;
    top: 104px;
    width: 500px;
    margin: 0;
    text-align: center;
    color: var(--ink);
  }
  .brand-claim .claim-main { display: block; font-size: 21px; letter-spacing: 0.5px; }
  .brand-claim .claim-sub { display: block; font-size: 19px; margin-top: 2px; }
  .mascot {
    position: absolute;
    left: 680px;
    top: 20px;
    width: 110px;
    height: 160px;
    border-radius: 55px 55px 14px 14px;
    background: linear-gradient(180deg, #b9a79c 0%, #efe7e1 40%, #c9cbd0 70%, #8e909a 100%);
  }
  .hero {
    position: absolute;
    left: 0;
    top: 160px;
    width: 850px;
    height: 470px;
  }
  .intro {
    position: absolute;
    left: 0;
    top: 641px;
    width: 850px;
    text-align: center;
  }
  .intro h2 {
    margin: 0;
    font-weight: 400;
    font-size: 28px;
    line-height: 34px;
    color: var(--teal-deep);
  }
  .intro .promise {
    margin: 6px 0 0;
    font-size: 23px;
    line-height: 28px;
    color: var(--teal-deep);
  }
  .intro .details {
    margin: 9px 0 0;
    font-size: 19px;
    line-height: 22px;
    color: var(--ink-soft);
  }
  .intro .details em { font-style: italic; }
  .services {
    position: absolute;
    left: 0;
    top: 850px;
    width: 850px;
    height: 190px;
    background: linear-gradient(180deg, #ececec 0%, #f7f7f5 100%);
  }
  .service-photo {
    position: absolute;
    top: 6px;
    width: 182px;
    height: 182px;
    border-radius: 50%;
    border: 6px solid #d4d6d8;
    box-shadow: 0 4px 8px rgba(0,0,0,0.15);
    box-sizing: border-box;
  }
  .service-photo.organising { left: 129px; background: linear-gradient(90deg, #f4efe9 0%, #e8b9c6 35%, #f3ede4 60%, #d9b99a 100%); }
  .service-photo.supplies { left: 334px; background: linear-gradient(160deg, #f2f3ea 0%, #cfe0b0 40%, #f0d76a 75%, #6f9a5a 100%); }
  .service-photo.windows { left: 539px; background: linear-gradient(200deg, #cfe6f5 0%, #9fcbe6 45%, #f0c84a 70%, #e8eef2 100%); }
  .tagline {
    position: absolute;
    left: 0;
    top: 1048px;
    width: 850px;
    margin: 0;
    text-align: center;
    font-size: 27px;
    line-height: 30px;
    color: var(--teal-deep);
  }
  .footer-rule {
    position: absolute;
    left: 0;
    top: 1124px;
    width: 850px;
    height: 4px;
    background: var(--teal);
  }
  .footer {
    position: absolute;
    left: 0;
    top: 1134px;
    width: 850px;
    height: 66px;
    background: var(--teal);
    color: var(--white);
    font-size: 28px;
  }
  .contact {
    position: absolute;
    top: 18px;
    display: flex;
    align-items: center;
    gap: 14px;
    line-height: 30px;
  }
  .contact.email { left: 54px; }
  .contact.phone { left: 470px; }
  .contact svg { width: 28px; height: 28px; }
  .social {
    position: absolute;
    top: 18px;
    width: 30px;
    height: 30px;
    border-radius: 50%;
    background: var(--lime);
  }
  .social.one { left: 766px; }
  .social.two { left: 802px; }
</style>
</head>
<body>
<main class="flyer">
  <header>
    <div class="brand-mark" aria-hidden="true"></div>
    <h1 class="brand-name">Tidy Nest Haven</h1>
    <p class="brand-claim">
      <span class="claim-main">EXPERIENCED AND FULLY INSURED</span>
      <span class="claim-sub">trustworthy and reliable</span>
    </p>
    <div class="mascot" role="img" aria-label="Illustration of a cheerful housekeeper in a maid uniform gesturing toward the title"></div>
  </header>

  <svg class="hero" viewBox="0 0 850 470">
    <defs>
      <linearGradient id="kitchenTone" x1="0" y1="0" x2="0" y2="1">
        <stop offset="0" stop-color="#e2e5e5"/>
        <stop offset="0.3" stop-color="#f4f4f2"/>
        <stop offset="0.45" stop-color="#9a9d9f"/>
        <stop offset="0.55" stop-color="#c8ad84"/>
        <stop offset="0.62" stop-color="#f3f3f1"/>
        <stop offset="1" stop-color="#dcdad5"/>
      </linearGradient>
    </defs>
    <path class="wave-lime-top" d="M0,80 C250,50 550,58 850,46 L850,60 C550,72 250,70 0,100 Z" fill="var(--lime)"/>
    <path class="wave-teal-top" d="M320,62 C520,42 700,22 850,4 L850,52 C700,56 520,60 320,62 Z" fill="var(--teal)"/>
    <path class="kitchen-photo" role="img" aria-label="Photo of a bright modern white kitchen with island and bar stools" d="M0,96 C250,70 550,76 850,60 L850,360 C600,385 300,395 0,378 Z" fill="url(#kitchenTone)"/>
    <path class="wave-lime-bottom" d="M0,384 C300,404 600,394 850,358 L850,372 C600,410 300,418 0,400 Z" fill="var(--lime)"/>
    <path class="wave-teal-bottom" d="M0,398 C200,424 420,440 850,384 L850,396 C500,462 200,462 0,446 Z" fill="var(--teal)"/>
  </svg>

  <section class="intro">
    <h2>Specialising in all Domestic Cleans and Home Organisation</h2>
    <p class="promise">Honest and trustworthy professional with references<br>available as well as being fully insured</p>
    <p class="details">I provide professional &amp; personalised Domestic Cleaning Services alongside<br>Home organisation. From weekly, monthly &amp; one-off spring cleans to tackling<br>bulging cupboards &amp; colour coordinating wardrobes.<br><em>Contact me today to arrange a free estimate.</em></p>
  </section>

  <section class="services">
    <div class="service-photo organising" role="img" aria-label="Photo of neatly organised shelves with boxes and folders"></div>
    <div class="service-photo supplies" role="img" aria-label="Photo of cleaning supplies, spray bottles and a lemon"></div>
    <div class="service-photo windows" role="img" aria-label="Photo of a hand wiping a window with a yellow cloth"></div>
  </section>

  <p class="tagline">Isn’t It About Time You Had More Time,<br>Well I’m Ready When You Are</p>

  <div class="footer-rule"></div>
  <footer class="footer">
    <div class="contact email">
      <svg viewBox="0 0 26 26" aria-hidden="true">
        <circle cx="13" cy="13" r="13" fill="var(--white)"/>
        <rect x="6.5" y="8.5" width="13" height="9" rx="1" fill="var(--teal)"/>
        <path d="M6.5,9 L13,14 L19.5,9" fill="none" stroke="var(--white)" stroke-width="1.4"/>
      </svg>
      <span>hello@tidynest-mail.com</span>
    </div>
    <div class="contact phone">
      <svg viewBox="0 0 26 26" aria-hidden="true">
        <circle cx="13" cy="13" r="13" fill="var(--white)"/>
        <path d="M9,7 L11.5,7 L12.5,10 L11,11.3 C11.8,13 13,14.2 14.7,15 L16,13.5 L19,14.5 L19,17 C19,18 18,19 17,19 C12,18.5 7.5,14 7,9 C7,8 8,7 9,7 Z" fill="var(--teal)"/>
      </svg>
      <span>07700900123</span>
    </div>
    <div class="social one" aria-hidden="true"></div>
    <div class="social two" aria-hidden="true"></div>
  </footer>
</main>
</body>
</html>
```